Website Redesign

I am looking to have our website redone. We recently paid to have this done and are very unhappy with the results. We're looking to have a much more modern and clean feeling while GREATLY enhancing the user experience. We are very close to have a new logo designed as well as having some brand colors (Pantone 3005C). We want our site to have a human feel to it without focusing completely on our products. That being said, we need our products to play a more prominent role as our current site doesn't very clearly display what we do.
Our website: kvhomewares.com
Websites we like (overall feel): jogluma.com, oswaldtrent.com
Websites we like (functionality): birchvault.com
Updates
I apologize, we are new to ArtHivePro. I am showing a budget of $500 for this project. I know we'd go beyond that. I do not believe that we'll be able to overhaul our website for $500. I apologize for any confusion.

```html
<!DOCTYPE html>
<html lang="en">
<head>
<meta charset="utf-8">
<title>KV Homewares — Commercial Furniture</title>
<link rel="stylesheet" href="https://fonts.googleapis.com/css2?family=Source+Sans+3:wght@300;400;600&display=swap">
<style>
  :root {
    --brand-blue: #0a77c9;
    --brand-blue-soft: #7fb6e2;
    --ink: #2b2b2b;
    --ink-muted: #4a4a4a;
    --header-bg: #f1f1f1;
    --panel-border: #d6d6d6;
    --panel-head: #f4f4f4;
    --footer-bg: #f2f2f2;
    --white: #ffffff;
  }
  * { box-sizing: border-box; margin: 0; padding: 0; }
  html, body { width: 1200px; height: 1008px; overflow: hidden; background: var(--white); }
  body { position: relative; font-family: "Source Sans 3", Arial, sans-serif; color: var(--ink); }
  a { color: inherit; text-decoration: none; }
  .abs { position: absolute; }

  /* Header */
  .site-header { position: absolute; left: 0; top: 0; width: 1200px; height: 120px;
    background: linear-gradient(#f7f7f7, #ececec); border-bottom: 8px solid #d9d9d9; }
  .brand { position: absolute; left: 130px; top: 34px; display: flex; align-items: center; gap: 8px;
    font-size: 26px; font-weight: 400; color: var(--brand-blue); }
  .brand-dot { width: 12px; height: 12px; border-radius: 50%; background: var(--brand-blue); }
  .utility-nav { position: absolute; top: 23px; left: 645px; font-size: 15px; color: var(--ink); display: flex; gap: 12px; }
  .search { position: absolute; left: 850px; top: 18px; width: 221px; height: 32px; border-radius: 16px;
    background: var(--white); border: 1px solid #cfcfcf; box-shadow: inset 0 1px 3px rgba(0,0,0,.12);
    font-size: 12px; color: #888; padding: 7px 0 0 17px; }
  .search svg { position: absolute; right: 9px; top: 6px; }
  .main-nav { position: absolute; top: 75px; left: 608px; display: flex; font-size: 15px; color: var(--brand-blue); letter-spacing: .2px; }
  .main-nav .sep { color: var(--brand-blue); margin: 0 30px; }

  /* Hero */
  .hero { position: absolute; left: 0; top: 120px; width: 1200px; height: 490px; overflow: hidden; }
  .hero-photo { position: absolute; inset: 0;
    background:
      radial-gradient(ellipse 200px 260px at 990px 300px, #3a2f2c 0%, #5a4a44 45%, rgba(200,190,180,0) 100%),
      linear-gradient(90deg, #d9d4cd 0%, #ece8e2 30%, #f3f0ec 55%, #e2ddd6 100%); }
  .hero-copy { position: absolute; left: 161px; top: 60px; width: 560px; }
  .hero-lead { font-size: 38px; font-weight: 300; line-height: 40px; color: var(--ink); }
  .hero-big { font-size: 78px; font-weight: 400; line-height: 66px; color: var(--brand-blue); letter-spacing: -.5px; }
  .hero-mid { font-size: 38px; font-weight: 300; line-height: 40px; color: var(--ink); width: 388px; text-align: right; }
  .hero-welcome { font-size: 31px; font-weight: 400; line-height: 34px; color: var(--ink); margin-top: 2px; }
  .hero-text { font-size: 17px; line-height: 23px; color: var(--brand-blue); margin-top: 6px; width: 560px; }
  .btn-more { position: absolute; left: 161px; top: 375px; width: 133px; height: 45px; border-radius: 23px;
    background: var(--brand-blue-soft); padding: 4px; }
  .btn-more span { display: block; height: 37px; border-radius: 19px; background: var(--brand-blue);
    color: var(--white); font-size: 18px; text-align: center; line-height: 37px; }
  .hero-arrows { position: absolute; left: 165px; top: 440px; }

  /* Panels */
  .panel { position: absolute; top: 633px; height: 249px; border: 1px solid var(--panel-border); border-radius: 10px; background: var(--white); overflow: hidden; }
  .panel-head { height: 44px; border-bottom: 1px solid var(--panel-border);
    background: linear-gradient(#fbfbfb, #efefef); font-size: 18px; line-height: 44px; }
  .categories { left: 130px; width: 620px; }
  .categories .panel-head { text-align: center; color: var(--brand-blue); }
  .panel-arrows { position: absolute; right: 14px; top: 14px; }
  .category { position: absolute; top: 54px; width: 169px; text-align: center; }
  .category-photo { width: 169px; height: 125px; border: 1px solid #d8d8d8; position: relative; }
  .category-photo .fill { position: absolute; inset: 6px; }
  .category-photo::after { content: ""; position: absolute; left: 76px; bottom: -9px; width: 14px; height: 14px;
    background: var(--white); border-right: 1px solid #d8d8d8; border-bottom: 1px solid #d8d8d8; transform: rotate(45deg); }
  .category-name { font-size: 14px; font-weight: 600; margin-top: 22px; letter-spacing: .3px; }
  .category-link { font-size: 12px; font-weight: 600; color: var(--brand-blue); margin-top: 4px; letter-spacing: .5px; }
  .contact { left: 770px; width: 300px; }
  .contact .panel-head { padding-left: 19px; color: var(--ink); }
  .contact-body { padding: 14px 0 0 20px; font-size: 15px; line-height: 24px; color: var(--ink-muted); }
  .contact-name { font-weight: 600; font-size: 16px; color: var(--ink); }
  .contact-name b { color: var(--brand-blue); font-weight: 600; }
  .contact-body .row { margin-top: 2px; }
  .contact-body a { color: var(--brand-blue); }

  /* Footer */
  .site-footer { position: absolute; left: 0; top: 905px; width: 1200px; height: 103px; background: var(--footer-bg); }
  .footer-links { position: absolute; left: 131px; top: 17px; font-size: 13px; color: var(--ink); display: flex; gap: 13px; }
  .copyright { position: absolute; left: 130px; top: 59px; font-size: 13px; color: var(--ink-muted); }
  .copyright a { color: var(--brand-blue); }
  .follow { position: absolute; left: 872px; top: 43px; font-size: 13px; color: var(--ink); display: flex; align-items: center; gap: 16px; }
  .social { width: 17px; height: 17px; border-radius: 50%; background: #7a7a7a; }
</style>
</head>
<body>

<header class="site-header">
  <a class="brand" href="#"><span class="brand-dot"></span>kv homewares</a>
  <nav class="utility-nav"><a href="#">Where to Buy</a><span>|</span><a href="#">Newsletters</a></nav>
  <div class="search">Search..
    <svg width="22" height="20" viewBox="0 0 22 20"><circle cx="8" cy="8" r="6" fill="none" stroke="#0a77c9" stroke-width="2.6"/><line x1="12.5" y1="12.5" x2="19" y2="18" stroke="#0a77c9" stroke-width="3.4" stroke-linecap="round"/></svg>
  </div>
  <nav class="main-nav">
    <a href="#">PRODUCTS</a><span class="sep">|</span>
    <a href="#">ORDERING</a><span class="sep">|</span>
    <a href="#">COMPANY</a><span class="sep">|</span>
    <a href="#">CONTACT</a>
  </nav>
</header>

<section class="hero">
  <div class="hero-photo" role="img" aria-label="Smiling businesswoman in a dark blazer standing in a bright, softly blurred office"></div>
  <div class="hero-copy">
    <p class="hero-lead">We Make Commerial</p>
    <p class="hero-big">FURNITURE</p>
    <p class="hero-mid">That’s inherently</p>
    <p class="hero-big">HUMAN</p>
    <h1 class="hero-welcome">WELCOME TO KIND VENUE</h1>
    <p class="hero-text">The last thing we think about when we’re creating new products, or refining old ones, is furniture. Because at KV Homewares, furniture is designed for people. So we start with them.</p>
  </div>
  <a class="btn-more" href="#"><span>MORE</span></a>
  <svg class="hero-arrows" width="64" height="38" viewBox="0 0 64 38">
    <polyline points="20,2 4,19 20,36" fill="none" stroke="#fff" stroke-width="4"/>
    <polyline points="42,2 58,19 42,36" fill="none" stroke="#fff" stroke-width="4"/>
  </svg>
</section>

<section class="panel categories">
  <h2 class="panel-head" style="font-weight:400">PRODUCT CATEGORIES</h2>
  <svg class="panel-arrows" width="40" height="16" viewBox="0 0 40 16">
    <polyline points="8,1 1,8 8,15" fill="none" stroke="#555" stroke-width="1.6"/>
    <polyline points="30,1 37,8 30,15" fill="none" stroke="#555" stroke-width="1.6"/>
  </svg>
  <div class="category" style="left:25px">
    <div class="category-photo"><div class="fill" role="img" aria-label="Round folding tables with wood-grain tops" style="background:radial-gradient(circle at 45% 55%, #b89a7a 0%, #8a6a4e 40%, #fff 72%)"></div></div>
    <p class="category-name">TABLES</p><p class="category-link">VIEW</p>
  </div>
  <div class="category" style="left:225px">
    <div class="category-photo"><div class="fill" role="img" aria-label="Black stacking chair with chrome sled base" style="background:radial-gradient(ellipse 40% 50% at 50% 45%, #333 0%, #777 45%, #fff 80%)"></div></div>
    <p class="category-name">SEATING</p><p class="category-link">VIEW</p>
  </div>
  <div class="category" style="left:425px">
    <div class="category-photo"><div class="fill" role="img" aria-label="Light wood lectern with dark front panel" style="background:radial-gradient(ellipse 30% 50% at 50% 50%, #c9ab88 0%, #5a4a3e 45%, #fff 85%)"></div></div>
    <p class="category-name">LECTERNS</p><p class="category-link">VIEW</p>
  </div>
</section>

<section class="panel contact">
  <h2 class="panel-head" style="font-weight:400">CONTACT INFO</h2>
  <div class="contact-body">
    <p class="contact-name"><b>KV</b> HOMEWARES</p>
    <p>418 Harbor Lane, Suite 210,<br>Lakeford,<br>WI 53999</p>
    <p class="row">Call Toll-free: <a href="#">800.555.0142</a></p>
    <p class="row">Fax: <a href="#">859.555.0178</a></p>
    <p class="row">Email: <a href="#">order@kvhomewares.com</a></p>
  </div>
</section>

<footer class="site-footer">
  <nav class="footer-links"><a href="#">Site Map</a><span>|</span><a href="#">Legal Terms of Use</a><span>|</span><a href="#">Privacy</a></nav>
  <p class="copyright">Copyright © 2013 <a href="#">KV Homewares</a>. All Right Reserved</p>
  <div class="follow">Follow Us:
    <span class="social" aria-label="Social link"></span>
    <span class="social" aria-label="Social link"></span>
    <span class="social" aria-label="Social link"></span>
    <span class="social" aria-label="Social link"></span>
  </div>
</footer>

</body>
</html>
```